Trellmark Vista brochure

A brochure based on the word document provided. Brochure provided in Word and PDF format. Should include pictures and shorten to make it a brochure of no more than two 8.5x11 pages. Completed brochure file must be under 5 megabytes.

Leadership

• final file size less than 5 megabytes. also file in Word and PDF and any other that makes sense. Must have pictures or graphics to support the text. Include the 3 logos attached from TKR, qoVantra, and Trellmark vista. qoVantra logo is in attachments you can get logo for Trellmark Vista at www.trellmarkvista.com. or http://www.trellmarkvista.com/images/logo.png

```html
<!DOCTYPE html>
<html lang="en">
<head>
<meta charset="utf-8">
<title>Trellmark Vista – About Membership</title>
<link href="https://fonts.googleapis.com/css2?family=Arimo:ital,wght@0,400;0,700;1,400&display=swap" rel="stylesheet">
<style>
  :root {
    --maroon: #9c1d3f;
    --tan: #c9b78f;
    --ink: #1d1d1d;
    --paper: #ffffff;
    --photo-a: #c7b4a3;
    --photo-b: #7a6258;
    --photo-c: #2f3a52;
  }
  * { margin: 0; padding: 0; box-sizing: border-box; }
  html, body { width: 926px; height: 1200px; overflow: hidden; background: var(--paper); }
  body { font-family: "Arimo", Arial, sans-serif; color: var(--ink); }
  .page { position: relative; width: 926px; height: 1200px; overflow: hidden; }

  .corner-tab { position: absolute; right: 0; top: 0; width: 44px; height: 44px; background: var(--tan); }

  .hero {
    position: absolute; left: 44px; top: 46px; width: 838px; height: 369px;
    border: 3px solid var(--maroon);
    background:
      radial-gradient(ellipse at 55% 40%, #e7d2c1 0%, transparent 45%),
      radial-gradient(ellipse at 85% 70%, var(--photo-c) 0%, transparent 40%),
      linear-gradient(120deg, #d9d2c8 0%, var(--photo-a) 40%, var(--photo-b) 75%, #3a3f52 100%);
  }
  .hero-title { position: absolute; left: 30px; bottom: 14px; color: #fff; line-height: 1; }
  .hero-title .light { display: block; font-size: 45px; font-weight: 400; letter-spacing: -0.5px; }
  .hero-title .bold { display: block; font-size: 47px; font-weight: 700; letter-spacing: -0.5px; margin-top: 2px; }

  .column { position: absolute; top: 454px; font-size: 13.3px; line-height: 16.4px; }
  .column-left { left: 44px; width: 410px; }
  .column-right { left: 481px; width: 402px; }
  .column p { margin-bottom: 17px; }
  .column strong { font-weight: 700; }
  .benefits { list-style: none; font-style: italic; margin: -2px 0 17px 22px; }
  .benefits li { position: relative; padding-left: 21px; margin-bottom: 4px; }
  .benefits li::before { content: "•"; position: absolute; left: 0; font-style: normal; }
  .column-right .benefits { margin: 0 0 17px 23px; }
  .column-right .section { margin-top: 26px; }

  .brand-block {
    position: absolute; left: 744px; top: 1017px; width: 138px; height: 139px;
    background: var(--maroon); display: flex; align-items: center; justify-content: center;
    padding: 0 14px; text-align: center;
  }
  .brand-name { color: #fff; font-size: 13px; line-height: 16px; font-weight: 400; }

  .footer-band { position: absolute; left: 44px; top: 1169px; width: 838px; height: 31px; background: var(--maroon); }
</style>
</head>
<body>
<main class="page">
  <div class="corner-tab"></div>

  <header class="hero" role="img" aria-label="Photo of a group of colleagues stacking their hands together in the center">
    <h1 class="hero-title"><span class="light">About</span><span class="bold">MEMBERSHIP</span></h1>
  </header>

  <section class="column column-left">
    <p><strong>Individual Membership</strong> – No cost. Sign up, participate, receive your own reports and use diary, attend webinars to learn about the results and how to use your own data and the overall findings. Receive benchmark data on key items for your business and industry. Be first to understand trends in the data.</p>
    <p><strong>Manager Associate Membership</strong> – This level of membership comes with a fee and is designed for managers who want to learn from their own data and group level data collected from their employees. There is an annual fee or $396 for this level of membership, and the fee can be paid annually (discount if paid once per year; fee is $350) or $396 if paid monthly ($33 per month).</p>
    <p>Manager and team membership includes all the benefits of individual members for the manager and all employees. In addition, the manager receives the following:</p>
    <ul class="benefits">
      <li>Manager level reports for all energy pulses; this includes aggregated data for all questions (other than personal diary items), on-line reporting, benchmark data and access to coaching calls and webinars for members only.</li>
      <li>Associate membership of the Tessaly Knowledge Research (TKR) at the Halvern School of Commerce, Wescombe State University. This membership comes with a badge designation level of accomplishment.</li>
      <li>As a manager associate, you will be invited to TKR webinars and other learning events (executive education programs, leadership summits, local meetings and more).</li>
      <li>You also will have access to the manager associate network of members.</li>
    </ul>
    <p><strong>Energy Pulsing (for individual and manager associate members)</strong> – Short, energy pulses will be sent out to the entire Trellmark Vista population every other month. The pulses will include 3 core questions to assess employee energy at work; in addition, other questions will focus on key business challenges identified by the research team at TKR and also by members. The data provided to individuals and managers are different from other sources of information in that the information is:</p>
    <ul class="benefits">
      <li>Trend data vs. point-in-time data; we teach managers about recovery techniques because data will fluctuate.</li>
    </ul>
  </section>

  <section class="column column-right">
    <ul class="benefits">
      <li>Energy data – energy predicts performance, so tracking energy will help you improve your own work and team’s performance. We teach you how to optimize and direct energy to be at your best and achieve goals.</li>
      <li>Topics important to drive high quality dialogue and learning – In the past we have studied confidence, entrepreneurial action and idea generation, business drivers, quality and more.</li>
      <li>As a member you will have input in the questions used; we ask what questions you think are important, and we include questions that are noted by multiple participants.</li>
      <li>Your data will include benchmarks on the overall sample, industry, firm size, amount of change the company is going through (this metric is an important benchmark demographic) and more.</li>
      <li>You will receive articles, press releases and technical reports on the overall learning.</li>
    </ul>
    <p class="section"><strong>Feedback, webinars and coaching conversations for manager associates</strong> – After each pulse, you will immediately receive your own personal reports and then when the data are aggregated (benchmarking available), you will receive your team and benchmark reports. In addition to all of the benefits of individual membership, you will be invited to webinars and coaching calls for manager associates only. In these more focused conversations, you can learn from the researchers at TKR, and also you can dialogue with peers who are facing similar challenges or opportunities.</p>
  </section>

  <div class="brand-block">
    <span class="brand-name">Tessaly Knowledge Research</span>
  </div>

  <div class="footer-band"></div>
</main>
</body>
</html>
```